LETTERHEAD & ENVELOPE: eye-catching stationary design for our custom office furniture business

Our company recently rebranded and we are in need of new stationary. Specifically, we need branded letterhead for standard paper size (8.5” x 11”), and matching envelopes, size: #9.

All designs should incorporate our brand colors, brand typeface, and logo. Please view attached brand guidelines document for brand colors, and brand description.

Letterhead: 8.5” x 11” Must include CedarlineKTV Logo, Talbot Greaves Certified Dealer Logo, mailing address, phone number, website, and email address.

Envelope: 9.5” x 4.125” Must include CedarlineKTV Logo, mailing address, and Talbot Greaves Certified Dealer Logo.

Attached files include:

```html
<!DOCTYPE html>
<html lang="en">
<head>
<meta charset="utf-8">
<title>CedarlineKTV — #9 Envelope</title>
<link rel="stylesheet" href="https://fonts.googleapis.com/css2?family=Raleway:wght@300;400&family=Arimo:wght@400&display=swap">
<style>
  :root {
    --backdrop: #ebebeb;
    --paper: #ffffff;
    --brand-green: #5b7d6f;
    --dealer-red: #e8381f;
    --ink-grey: #5a5a5a;
  }
  * { margin: 0; padding: 0; box-sizing: border-box; }
  html, body {
    width: 1200px;
    height: 1012px;
    overflow: hidden;
    background: var(--backdrop);
  }
  .stationery {
    position: relative;
    width: 1200px;
    height: 1012px;
  }
  .envelope {
    position: absolute;
    left: 239px;
    width: 707px;
    height: 324px;
    background: var(--paper);
    overflow: hidden;
  }
  .envelope--back { top: 160px; }
  .envelope--front { top: 525px; }
  .envelope__flap {
    position: absolute;
    left: 0;
    top: 0;
  }
  .brand-mark {
    position: absolute;
    left: 43px;
    top: 31px;
    width: 38px;
    height: 38px;
    border-radius: 50%;
    background: var(--brand-green);
  }
  .brand-name {
    position: absolute;
    left: 94px;
    top: 34px;
    font-family: "Raleway", sans-serif;
    font-weight: 300;
    font-size: 29px;
    line-height: 32px;
    color: var(--brand-green);
    letter-spacing: 0.2px;
  }
  .return-address {
    position: absolute;
    left: 96px;
    top: 76px;
    font-family: "Arimo", sans-serif;
    font-size: 9px;
    line-height: 12px;
    color: var(--ink-grey);
    font-style: normal;
  }
  .dealer-badge {
    position: absolute;
    left: 43px;
    top: 262px;
    width: 30px;
    height: 30px;
    border-radius: 50%;
    background: var(--dealer-red);
  }
  .dealer-name {
    position: absolute;
    left: 82px;
    top: 268px;
    font-family: "Raleway", sans-serif;
    font-weight: 400;
    font-size: 14px;
    line-height: 18px;
    color: var(--dealer-red);
  }
</style>
</head>
<body>
  <main class="stationery">
    <section class="envelope envelope--back" aria-label="Envelope back">
      <svg class="envelope__flap" width="707" height="324" viewBox="0 0 707 324" aria-hidden="true">
        <path d="M0 0 H707 L694 92 Q689 112 668 112 H39 Q18 112 13 92 Z" fill="var(--brand-green)"/>
      </svg>
    </section>

    <section class="envelope envelope--front" aria-label="Envelope front">
      <div class="brand-mark" aria-hidden="true"></div>
      <div class="brand-name">CedarlineKTV</div>
      <address class="return-address">
        410 SE Alder Row, Suite 112<br>
        Lakemont, OR 97018
      </address>
      <div class="dealer-badge" aria-hidden="true"></div>
      <div class="dealer-name">Talbot Greaves Certified Dealer</div>
    </section>
  </main>
</body>
</html>
```